Android Game Graphics
Puzzle Game Buttons/Background
I'm developing a puzzle game for android and I need a fun/colorful background and several buttons. I have attached sketches of the three screens I need graphics for.
The winning logo must "pop" like the "fuzzy otters" graphics. The graphics need to be fun and colorful, but I have no formal requirements. The game is a clone of the classic game "Glyphwalk". You can see/play the original game here: http://marlowjpenfield.com/android/games/glyphwalk.swf Below I have sketches of the three screens in the game, please make these with colorful graphics and buttons. For the first and second images, make sure the background image has "Quill Quest" somewhere spanning the back. For the third image, the one with the letters, make all of the letters/tiles the same color. Wood color like tilzor would probably be the best, but I'm open to suggestions. Also where "Quill Quest" is on the third image, make some sort of cartoony logo. I was thinking maybe the word formed from some sort of cartoony worm with glasses, but again, it's up to you. Please make all of the buttons, including the letters individually and high res because they will eventually be used on a 10 inch (1280 x 800 resolution tablet). Screen 1: http://img811.pixelcrate.net/i/introscreen1.png/ Screen 2: http://img827.pixelcrate.net/i/selectgame2.png/ Screen 3: http://img573.pixelcrate.net/i/gameplay3.png/ Basically, make the three images above how you think the game and menu should look. The resolution in the attached images is 854 x 480, but make sure you make them for a higher res tablet.

```html
<!DOCTYPE html>
<html lang="en">
<head>
<meta charset="utf-8">
<title>Quill Quest – Game Board</title>
<link href="https://fonts.googleapis.com/css2?family=Bangers&family=Luckiest+Guy&display=swap" rel="stylesheet">
<style>
  :root{
    --sky-deep:#1f63c9;
    --sky-mid:#3f8ff0;
    --sky-light:#a9d8ff;
    --wood-light:#f0c98a;
    --wood-mid:#d99f55;
    --wood-dark:#8a5a24;
    --wood-edge:#5b3612;
    --ink:#141414;
    --panel:#1a4fb8;
    --panel-edge:#0d2f78;
    --dirt-top:#a05a24;
    --dirt-low:#5c2f10;
    --logo:#ffd21f;
    --red:#e0231b;
    --green:#2f9e1e;
    --blue:#1d3fa8;
    --gold:#f5c400;
    --pink:#ff2f86;
  }
  *{box-sizing:border-box;margin:0;padding:0}
  html,body{width:1200px;height:785px;overflow:hidden;background:#fff}
  .board{
    position:relative;width:1200px;height:785px;overflow:hidden;
    background:radial-gradient(circle at 40% 35%,var(--sky-light) 0%,var(--sky-mid) 45%,var(--sky-deep) 100%);
  }
  .ground{
    position:absolute;left:0;bottom:0;width:850px;height:190px;
  }
  .tile-field{position:absolute;left:44px;top:0;width:790px;height:700px}
  .column{position:absolute;display:flex;flex-direction:column;gap:4px;width:74px}
  .tile{
    position:relative;width:74px;height:84px;border-radius:9px;
    background:linear-gradient(160deg,var(--wood-light) 0%,var(--wood-mid) 70%,var(--wood-dark) 100%);
    border:3px solid var(--wood-edge);
    box-shadow:inset 0 0 0 3px rgba(255,235,190,.55),2px 3px 0 rgba(0,0,0,.35);
    font-family:"Bangers",cursive;color:var(--ink);
  }
  .tile .letter{position:absolute;left:0;right:6px;top:6px;text-align:center;font-size:58px;line-height:1}
  .tile .points{position:absolute;right:6px;bottom:3px;font-size:19px;line-height:1}
  .side-panel{
    position:absolute;left:848px;top:14px;width:340px;height:762px;border-radius:14px;
    background:linear-gradient(180deg,var(--sky-mid),var(--panel));
    border:4px solid var(--panel-edge);
  }
  .post{position:absolute;left:158px;top:190px;width:22px;height:560px;background:linear-gradient(90deg,var(--wood-dark),var(--wood-mid),var(--wood-dark));border:2px solid var(--wood-edge)}
  .logo{
    position:absolute;left:12px;top:6px;width:310px;text-align:center;
    font-family:"Luckiest Guy",cursive;color:var(--logo);font-size:64px;line-height:.95;
  }
  .sign{
    position:absolute;display:flex;align-items:center;justify-content:center;
    border-radius:8px;border:3px solid var(--wood-edge);
    background:linear-gradient(180deg,var(--wood-light),var(--wood-mid) 80%,var(--wood-dark));
    box-shadow:2px 3px 0 rgba(0,0,0,.35);
    font-family:"Luckiest Guy",cursive;letter-spacing:1px;
  }
  .sign-score{left:22px;top:200px;width:290px;height:80px;font-size:40px;color:var(--ink)}
  .sign-word{left:22px;top:284px;width:290px;height:56px;font-size:26px;color:var(--red)}
  .sign-points{left:22px;top:342px;width:290px;height:56px;font-size:26px;color:var(--green)}
  .sign-level{left:22px;top:410px;width:290px;height:70px;font-size:32px;color:var(--blue)}
  .sign-clear{left:22px;top:496px;width:120px;height:62px;font-size:28px;color:var(--gold)}
  .sign-scramble{left:150px;top:496px;width:162px;height:62px;font-size:24px;color:var(--red)}
  .sign-submit{left:22px;top:594px;width:290px;height:96px;font-size:46px;color:var(--pink)}
</style>
</head>
<body>
<main class="board">
  <svg class="ground" viewBox="0 0 850 190" role="img" aria-label="Cartoon underground dirt tunnel with pebbles and ants">
    <defs>
      <linearGradient id="dirt" x1="0" y1="0" x2="0" y2="1">
        <stop offset="0" stop-color="#a05a24"/>
        <stop offset="1" stop-color="#5c2f10"/>
      </linearGradient>
    </defs>
    <path d="M0 40 Q220 0 430 30 T850 20 V190 H0 Z" fill="url(#dirt)"/>
  </svg>

  <section class="tile-field">
    <div class="column" style="left:0;top:56px">
      <div class="tile"><span class="letter">A</span><span class="points">1</span></div>
      <div class="tile"><span class="letter">K</span><span class="points">5</span></div>
      <div class="tile"><span class="letter">U</span><span class="points">4</span></div>
      <div class="tile"><span class="letter">E</span><span class="points">1</span></div>
      <div class="tile"><span class="letter">O</span><span class="points">1</span></div>
      <div class="tile"><span class="letter">Y</span><span class="points">4</span></div>
    </div>
    <div class="column" style="left:79px;top:96px">
      <div class="tile"><span class="letter">B</span><span class="points">3</span></div>
      <div class="tile"><span class="letter">L</span><span class="points">1</span></div>
      <div class="tile"><span class="letter">V</span><span class="points">4</span></div>
      <div class="tile"><span class="letter">F</span><span class="points">4</span></div>
      <div class="tile"><span class="letter">P</span><span class="points">3</span></div>
      <div class="tile"><span class="letter">Z</span><span class="points">10</span></div>
    </div>
    <div class="column" style="left:158px;top:56px">
      <div class="tile"><span class="letter">C</span><span class="points">3</span></div>
      <div class="tile"><span class="letter">M</span><span class="points">3</span></div>
      <div class="tile"><span class="letter">W</span><span class="points">4</span></div>
      <div class="tile"><span class="letter">G</span><span class="points">2</span></div>
      <div class="tile"><span class="letter">Q</span><span class="points">10</span></div>
      <div class="tile"><span class="letter">A</span><span class="points">1</span></div>
    </div>
    <div class="column" style="left:237px;top:96px">
      <div class="tile"><span class="letter">D</span><span class="points">2</span></div>
      <div class="tile"><span class="letter">N</span><span class="points">1</span></div>
      <div class="tile"><span class="letter">X</span><span class="points">8</span></div>
      <div class="tile"><span class="letter">H</span><span class="points">4</span></div>
      <div class="tile"><span class="letter">R</span><span class="points">1</span></div>
      <div class="tile"><span class="letter">B</span><span class="points">3</span></div>
    </div>
    <div class="column" style="left:316px;top:56px">
      <div class="tile"><span class="letter">E</span><span class="points">1</span></div>
      <div class="tile"><span class="letter">O</span><span class="points">1</span></div>
      <div class="tile"><span class="letter">Y</span><span class="points">4</span></div>
      <div class="tile"><span class="letter">I</span><span class="points">1</span></div>
      <div class="tile"><span class="letter">S</span><span class="points">1</span></div>
      <div class="tile"><span class="letter">C</span><span class="points">3</span></div>
    </div>
    <div class="column" style="left:395px;top:96px">
      <div class="tile"><span class="letter">F</span><span class="points">4</span></div>
      <div class="tile"><span class="letter">P</span><span class="points">3</span></div>
      <div class="tile"><span class="letter">Z</span><span class="points">10</span></div>
      <div class="tile"><span class="letter">J</span><span class="points">8</span></div>
      <div class="tile"><span class="letter">T</span><span class="points">1</span></div>
      <div class="tile"><span class="letter">D</span><span class="points">2</span></div>
    </div>
    <div class="column" style="left:474px;top:56px">
      <div class="tile"><span class="letter">G</span><span class="points">2</span></div>
      <div class="tile"><span class="letter">Q</span><span class="points">10</span></div>
      <div class="tile"><span class="letter">A</span><span class="points">1</span></div>
      <div class="tile"><span class="letter">K</span><span class="points">5</span></div>
      <div class="tile"><span class="letter">U</span><span class="points">1</span></div>
      <div class="tile"><span class="letter">E</span><span class="points">1</span></div>
    </div>
    <div class="column" style="left:553px;top:96px">
      <div class="tile"><span class="letter">H</span><span class="points">4</span></div>
      <div class="tile"><span class="letter">R</span><span class="points">1</span></div>
      <div class="tile"><span class="letter">B</span><span class="points">3</span></div>
      <div class="tile"><span class="letter">L</span><span class="points">1</span></div>
      <div class="tile"><span class="letter">V</span><span class="points">4</span></div>
      <div class="tile"><span class="letter">F</span><span class="points">4</span></div>
    </div>
    <div class="column" style="left:632px;top:56px">
      <div class="tile"><span class="letter">I</span><span class="points">1</span></div>
      <div class="tile"><span class="letter">S</span><span class="points">1</span></div>
      <div class="tile"><span class="letter">C</span><span class="points">3</span></div>
      <div class="tile"><span class="letter">M</span><span class="points">3</span></div>
      <div class="tile"><span class="letter">W</span><span class="points">4</span></div>
      <div class="tile"><span class="letter">G</span><span class="points">2</span></div>
    </div>
    <div class="column" style="left:711px;top:96px">
      <div class="tile"><span class="letter">J</span><span class="points">8</span></div>
      <div class="tile"><span class="letter">T</span><span class="points">1</span></div>
      <div class="tile"><span class="letter">D</span><span class="points">2</span></div>
      <div class="tile"><span class="letter">N</span><span class="points">1</span></div>
      <div class="tile"><span class="letter">X</span><span class="points">8</span></div>
      <div class="tile"><span class="letter">H</span><span class="points">4</span></div>
    </div>
  </section>

  <aside class="side-panel">
    <div class="post"></div>
    <h1 class="logo">Quill<br>Quest</h1>
    <div class="sign sign-score">Score:</div>
    <div class="sign sign-word">Current Word</div>
    <div class="sign sign-points">Your Points</div>
    <div class="sign sign-level">Level 10</div>
    <div class="sign sign-clear">Clear</div>
    <div class="sign sign-scramble">Scramble</div>
    <div class="sign sign-submit">Submit</div>
  </aside>
</main>
</body>
</html>
```